依頼詳細
ラベルのデザインを募集します。

基本的には、幅91.5mm 縦131mmの縦長で角が少し丸いシールにいれるデザインです
・データは様々な形で使用させて頂きます。
(ホームページに載せたり、サンプル品に使用するなど)

クラフトのチャック袋(スタンドパック)にラベルを貼る予定です。
■キャッチフレーズなど
・魔法のスーパーフード タイガーナッツ!パウダータイプ

記載項目
商品名:星屑のコモレビパウダー
その他キャッチフレーズ、キーワードなど:スーパーフード
希望イメージ
シンプル 複雑
単色 カラフル
暗い 明るい
日常 高級
遊び心 厳粛
未来的 伝統的
女性的 男性的
希望する色
赤系、黄・オレンジ系
納品ファイル
• イラストレーター形式 (.ai)
• フォトショップ形式 (.psd)
補足説明
送付ファイルはパウダーの写真です。特に使わなくても大丈夫ですが、色合いなど確認するのにお使いください。
粒状態の画像を追加します。
製品自体は粉なので参考にしてください。
使わなくても大丈夫です。
■ 選んだ理由

自分の考えていたイメージに近く、魔法感がよく出ていて
まとまっていたのでこちらを選ばせて頂きました。

■ 提案者全員のお礼・コメント

多数のご応募ありがとうございました。
またの機会がありましたら、よろしくお願い足します。

```html
<!DOCTYPE html>
<html lang="ja">
<head>
<meta charset="utf-8">
<title>星屑のコモレビパウダー ラベル</title>
<link href="https://fonts.googleapis.com/css2?family=M+PLUS+1p:wght@800;900&family=Noto+Serif+JP:wght@700;900&display=swap" rel="stylesheet">
<style>
  :root {
    --orange-deep: #f08a12;
    --orange-mid: #f7a823;
    --orange-light: #fcc861;
    --cream: #fffdf6;
    --red: #e23a1c;
    --ink: #1a1a1a;
    --badge: #f5a31a;
    --powder: #b39a72;
    --lamp: #d9ab3c;
  }
  * { margin: 0; padding: 0; box-sizing: border-box; }
  html, body { width: 836px; height: 1200px; overflow: hidden; background: #ffffff; }
  .label {
    position: relative;
    width: 836px; height: 1200px;
    border: 3px solid var(--ink);
    border-radius: 36px;
    overflow: hidden;
    background: radial-gradient(circle at 52% 42%, var(--orange-light) 0%, var(--orange-mid) 45%, var(--orange-deep) 100%);
    font-family: "M PLUS 1p", sans-serif;
  }
  .top-band {
    position: absolute; left: 0; top: 0; width: 100%; height: 200px;
    background: var(--cream);
    border-bottom-left-radius: 50% 60px;
    border-bottom-right-radius: 50% 60px;
  }
  .wand-art {
    position: absolute; left: 0; top: 0; width: 210px; height: 180px;
    background: radial-gradient(circle at 40% 45%, #f3c04a 0%, #d89220 55%, rgba(216,146,32,0) 75%);
  }
  .bubble { position: absolute; left: 40px; top: 170px; width: 780px; height: 720px; }
  .kicker {
    position: absolute; top: 112px; left: 250px;
    font-size: 46px; font-weight: 900; color: var(--ink); letter-spacing: 1px;
  }
  .badge {
    position: absolute; border-radius: 50%;
    background: var(--badge); color: var(--ink);
    display: flex; align-items: center; justify-content: center;
    font-weight: 800; font-size: 25px;
  }
  .badge-skin { left: 560px; top: 160px; width: 130px; height: 130px; }
  .badge-diet { left: 660px; top: 225px; width: 150px; height: 150px; }
  .title {
    position: absolute; left: 0; width: 100%; text-align: center;
    font-family: "Noto Serif JP", serif; font-weight: 900; color: var(--red);
    paint-order: stroke fill; -webkit-text-stroke: 10px #ffffff;
    text-shadow: 0 0 3px rgba(0,0,0,0.25);
  }
  .title-lead { top: 290px; left: -110px; font-size: 92px; font-style: italic; }
  .title-main { top: 400px; font-size: 138px; letter-spacing: 4px; }
  .title-sub { top: 545px; font-size: 118px; letter-spacing: 6px; }
  .tagline {
    position: absolute; top: 705px; left: 0; width: 100%; text-align: center;
    font-family: "Noto Serif JP", serif; font-weight: 900;
    font-size: 42px; color: var(--ink);
  }
  .powder-photo {
    position: absolute; left: 42px; top: 795px; width: 252px; height: 252px;
    background: radial-gradient(circle at 45% 45%, #c9b08a 0%, var(--powder) 60%, #8e7552 100%);
  }
  .lamp-art {
    position: absolute; left: 495px; top: 915px; width: 260px; height: 230px;
    background: radial-gradient(ellipse at 50% 60%, #f4d376 0%, var(--lamp) 50%, rgba(217,171,60,0) 78%);
  }
  .usage {
    position: absolute; left: 42px; top: 1062px;
    font-size: 29px; font-weight: 900; color: var(--ink); line-height: 1.45;
  }
</style>
</head>
<body>
  <div class="label">
    <div class="top-band"></div>
    <div class="wand-art" role="img" aria-label="きらめく星の魔法の杖のイラスト"></div>

    <svg class="bubble" viewBox="0 0 780 720" aria-hidden="true">
      <path d="M390 10 C600 10 760 140 760 330 C760 520 600 640 400 650 C330 654 270 645 215 628 L60 715 L120 590 C40 530 10 440 10 330 C10 140 180 10 390 10 Z" fill="#ffffff"/>
    </svg>

    <p class="kicker">話題のスーパーフード</p>
    <div class="badge badge-skin">美肌に</div>
    <div class="badge badge-diet">ダイエットに</div>

    <h1>
      <span class="title title-lead">星屑の</span>
      <span class="title title-main">コモレビ</span>
      <span class="title title-sub">パウダー</span>
    </h1>
    <p class="tagline">栄養豊富、低カロリー</p>

    <div class="powder-photo" role="img" aria-label="パウダーの写真"></div>
    <div class="lamp-art" role="img" aria-label="金色の魔法のランプのイラスト"></div>

    <p class="usage">パウダータイプだから<br>ヨーグルトやスムージー<br>に混ぜてもOK!</p>
  </div>
</body>
</html>
```